Market Research firm needs updated business cards with new logo

We need the logo to be included somewhere on the card (attached). We would also like the phrases "Independent, Objective, Comprehensive" and "Research You Can Trust" somewhere on the card. Front or back. Our colors are hex codes 6075a7, e48d25 and 5a5b5b. Though you are certainly not limited to those shades, whatever you produce should coordinate with them. I have also attached our favicon. Feel free to use it in your design, but please do not use it to replace the full logo.

Contact Information for Business Card

see project description

Font styles to use
Other font styles liked:
• Open Sans

Requirements
Must have
• the logo
• We use Open Sans font

```html
<!DOCTYPE html>
<html lang="en">
<head>
<meta charset="utf-8">
<title>Norvale Research – Business Card</title>
<link href="https://fonts.googleapis.com/css2?family=Open+Sans:wght@400;600&display=swap" rel="stylesheet">
<style>
  :root {
    --brand-blue: #6075a7;
    --brand-orange: #e48d25;
    --brand-grey: #5a5b5b;
    --white: #ffffff;
    --bg-start: #000000;
    --bg-end: #022b2b;
  }
  * { margin: 0; padding: 0; box-sizing: border-box; }
  html, body { width: 1200px; height: 1200px; overflow: hidden; }
  body {
    position: relative;
    background: linear-gradient(90deg, var(--bg-start), var(--bg-end));
    font-family: "Open Sans", Arial, sans-serif;
  }
  .card {
    position: absolute;
    left: 180px;
    width: 840px;
    height: 480px;
    border-radius: 22px;
    overflow: hidden;
  }
  .card--front { top: 104px; background: var(--brand-grey); }
  .card--back { top: 616px; background: var(--brand-blue); }

  .wordmark {
    position: absolute;
    font-weight: 600;
    white-space: nowrap;
    letter-spacing: -1px;
    line-height: 1;
  }
  .card--front .wordmark {
    left: 150px; top: 44px;
    font-size: 68px;
    color: var(--brand-orange);
  }
  .card--back .wordmark {
    left: 60px; top: 172px;
    font-size: 84px;
    color: var(--white);
  }

  .mark-circle {
    position: absolute;
    left: 44px; top: 204px;
    width: 240px; height: 240px;
    border: 13px solid var(--white);
    border-radius: 50%;
  }

  .contact-list { list-style: none; }
  .contact-item {
    position: absolute;
    right: 56px;
    display: flex;
    align-items: center;
    gap: 38px;
    color: var(--white);
    white-space: nowrap;
    line-height: 1.2;
  }
  .contact-item .text { text-align: right; }
  .contact-item--phone { top: 190px; font-size: 36px; }
  .contact-item--fax   { top: 264px; font-size: 36px; }
  .contact-item--email { top: 338px; font-size: 30px; }
  .contact-item--web   { top: 404px; font-size: 30px; }
  .icon { width: 48px; height: 48px; flex: none; }

  .tagline {
    position: absolute;
    top: 292px;
    font-size: 23px;
    color: var(--white);
    white-space: nowrap;
  }
  .tagline--independent { left: 28px; }
  .tagline--objective { left: 220px; }
  .tagline--comprehensive { left: 340px; }
  .tagline--trust { left: 548px; }
</style>
</head>
<body>
  <section class="card card--front">
    <div class="wordmark">Norvale Research</div>
    <div class="mark-circle"></div>
    <ul class="contact-list">
      <li class="contact-item contact-item--phone">
        <span class="text">418 203 771</span>
        <svg class="icon" viewBox="0 0 48 48" aria-hidden="true">
          <circle cx="24" cy="24" r="23" fill="var(--brand-orange)"/>
          <path d="M16 13c2-1 3 0 4 2l2 4c0 1.5-1 2.5-2 3 1 3 3 5 6 6 .5-1 1.5-2 3-2l4 2c2 1 3 2 2 4-1 3-4 4-7 3-7-2-12-7-14-14-.8-3 0-6 2-8z" fill="var(--brand-grey)"/>
        </svg>
      </li>
      <li class="contact-item contact-item--fax">
        <span class="text">418 392 064</span>
        <svg class="icon" viewBox="0 0 48 48" fill="none" stroke="var(--brand-orange)" stroke-width="2.4" aria-hidden="true">
          <rect x="14" y="3" width="20" height="20"/>
          <path d="M18 9h12M18 13h12M18 17h12"/>
          <rect x="2" y="23" width="44" height="22" rx="3"/>
          <path d="M13 39c0-7 22-7 22 0" stroke-width="4"/>
        </svg>
      </li>
      <li class="contact-item contact-item--email">
        <span class="text">youremail@mailbox.com</span>
        <svg class="icon" viewBox="0 0 48 48" fill="none" stroke="var(--brand-orange)" stroke-width="2.6" aria-hidden="true">
          <rect x="2" y="8" width="44" height="34" rx="3"/>
          <path d="M3 10l21 18 21-18M3 40l16-14M45 40L29 26"/>
        </svg>
      </li>
      <li class="contact-item contact-item--web">
        <span class="text">www.yourweb.com</span>
        <svg class="icon" viewBox="0 0 48 48" fill="none" stroke="var(--brand-orange)" stroke-width="2.6" aria-hidden="true">
          <circle cx="24" cy="24" r="22"/>
          <ellipse cx="24" cy="24" rx="9" ry="22"/>
          <path d="M2 24h44M24 2v44M6 13h36M6 35h36"/>
        </svg>
      </li>
    </ul>
  </section>

  <section class="card card--back">
    <div class="wordmark">Norvale Research</div>
    <span class="tagline tagline--independent">Independent</span>
    <span class="tagline tagline--objective">Objective</span>
    <span class="tagline tagline--comprehensive">Comprehensive</span>
    <span class="tagline tagline--trust">Research You Can Trust</span>
  </section>
</body>
</html>
```